Catholic composer needs poster for new musical, "THE STONE AND THE VIGIL, the Harvest Musical"

We need a dynamic poster for "The Stone and the Vigil," a new musical written for Catholic dinner theater. We need you to create an iconic design like you see in posters for classic musicals, like "Rosa Calendula," Lantern of the Harbour," or "Gilded." In our musical, “fire” represents the Holy Spirit, who showers man with his merciful love.

Miraculous events occur. A mighty wind from heaven fills the house. Tongues of fire appear over their heads. They speak in other tongues that are understandable by all present. They are emboldened to go out and tell the Good News to the world, despite the risks associated with evangelizing this fledgling religion. They exclaim, “Lord, you will show us the path to life.”

Target Market(s)

The audience is adult members of Catholic churches. But don't make the design look too "churchy."

Requirements
Must have
• Photoshop or Illustrated file with layers, or vector format.
Should not have
• Really don't want photos.

```html
<!DOCTYPE html>
<html lang="en">
<head>
<meta charset="utf-8">
<title>The Stone and the Vigil – The Harvest Musical</title>
<link rel="stylesheet" href="https://fonts.googleapis.com/css2?family=Oswald:wght@400;500&display=swap">
<style>
  :root {
    --crimson: #b1283b;
    --flame: #f26d45;
    --cream: #fbe9c8;
  }
  html, body {
    margin: 0;
    padding: 0;
    overflow: hidden;
    background: var(--crimson);
  }
  .poster {
    position: relative;
    width: 851px;
    height: 1200px;
    background: var(--crimson);
    color: var(--flame);
    font-family: "Oswald", "Arial Narrow", sans-serif;
    overflow: hidden;
  }
  .emblem-area {
    position: absolute;
    left: 375px;
    top: 112px;
    width: 100px;
    height: 100px;
    background: var(--flame);
  }
  .title {
    position: absolute;
    left: 0;
    top: 275px;
    width: 100%;
    margin: 0;
    text-align: center;
    font-weight: 500;
    font-size: 138px;
    line-height: 190px;
    letter-spacing: 2px;
  }
  .title span { display: block; }
  .credits {
    position: absolute;
    left: 210px;
    top: 826px;
    margin: 0;
    font-weight: 500;
    text-transform: uppercase;
    line-height: 1.3;
  }
  .credits .subtitle { font-size: 18px; letter-spacing: 4px; display: block; }
  .credits .genre { font-size: 22px; letter-spacing: 0.5px; display: block; }
  .credits .author { font-size: 27px; letter-spacing: 2px; display: block; padding-left: 18px; }
  .tagline {
    position: absolute;
    left: 0;
    top: 982px;
    width: 100%;
    margin: 0;
    text-align: center;
    color: var(--cream);
    font-weight: 500;
    font-size: 25px;
    letter-spacing: 1px;
    text-transform: uppercase;
  }
  .details {
    position: absolute;
    left: 40px;
    right: 40px;
    top: 1058px;
    display: flex;
    justify-content: space-between;
    font-size: 22px;
    letter-spacing: 1px;
    text-transform: uppercase;
  }
  .details span { width: 190px; }
  .website {
    position: absolute;
    left: 0;
    top: 1110px;
    width: 100%;
    text-align: center;
    font-size: 16px;
    letter-spacing: 17.5px;
    text-transform: uppercase;
  }
</style>
</head>
<body>
  <main class="poster">
    <div class="emblem-area" role="img" aria-label="Emblem of the musical"></div>

    <h1 class="title">
      <span>THE STONE</span>
      <span>AND</span>
      <span>THE VIGIL</span>
    </h1>

    <p class="credits">
      <span class="subtitle">The Harvest Musical</span>
      <span class="genre">A new musical for Catholic dinner theater</span>
      <span class="author">By Nolan Briscoe</span>
    </p>

    <p class="tagline">“O Spirit come, you are merciful love”</p>

    <div class="details">
      <span>Where:</span>
      <span>Date:</span>
      <span>Time:</span>
      <span>Ticket prices:</span>
    </div>

    <div class="website">www.thestoneandthevigil.com</div>
  </main>
</body>
</html>
```